Trakvane Trade Show Booth Media Walls

Design two complementary 3m × 2.2m trade show media walls for Trakvane, a digital safety and compliance platform for Australian heavy vehicle operators. The booth should feel premium, modern, and highly readable from a trade show aisle, using Trakvane’s dark navy, white, bright cyan, and subtle green accent visual style.
Wall 1 should be a bold hero/brand wall that attracts attention and communicates Trakvane’s core message. Wall 2 should be a proof/product wall that shows the breadth of the platform and supports sales conversations. Please use the uploaded PDF brief, supplied brand assets, product references, and printer template for full design direction and production requirements

```html
<!DOCTYPE html>
<html lang="en">
<head>
<meta charset="utf-8">
<title>Trakvane Trade Show Media Walls</title>
<link rel="stylesheet" href="https://fonts.googleapis.com/css2?family=Inter:wght@400;500;600;700;800&family=Poppins:wght@400;500&display=swap">
<style>
  :root {
    --page: #ffffff;
    --navy: #02112a;
    --card: #061b3a;
    --cyan: #10a6cb;
    --line: #1a6f8e;
    --white: #ffffff;
    --soft: #dfe6ee;
  }
  * { box-sizing: border-box; margin: 0; padding: 0; }
  html, body { width: 1200px; height: 1200px; overflow: hidden; background: var(--page); }
  body { position: relative; font-family: "Inter", sans-serif; color: var(--white); }

  .wall { position: absolute; left: 222px; width: 756px; height: 554px; background: var(--navy); }
  .wall--hero { top: 50px; }
  .wall--proof { top: 624px; }

  .brand { position: absolute; left: 53px; top: 44px; display: flex; align-items: center; gap: 8px; }
  .brand__dot { width: 18px; height: 18px; border-radius: 50%; background: var(--cyan); }
  .brand__name { font-size: 21px; font-weight: 400; letter-spacing: -0.2px; color: var(--white); line-height: 1; }

  .tagline { position: absolute; left: 53px; top: 97px; font-size: 13px; font-weight: 700; color: var(--cyan); line-height: 15.5px; }

  .visual-area { position: absolute; left: 53px; top: 146px; width: 318px; height: 294px; border: 1.5px dashed var(--soft);
    display: flex; flex-direction: column; align-items: center; justify-content: center; text-align: center;
    font-size: 12.5px; font-weight: 600; color: var(--soft); line-height: 15.5px; padding-bottom: 10px; }
  .visual-area p + p { margin-top: 16px; }

  .headline { position: absolute; left: 385px; font-size: 36px; font-weight: 800; line-height: 32px; letter-spacing: -0.2px; }
  .headline span { display: block; }
  .headline .accent { color: var(--cyan); }
  .headline--1 { top: 128px; }
  .headline--2 { top: 229px; }
  .headline--3 { top: 329px; }

  .feature-bar { position: absolute; left: 62px; top: 458px; width: 630px; height: 37px; border: 1px solid var(--line); border-radius: 7px;
    display: flex; align-items: center; justify-content: space-between; padding: 0 16px 0 12px; }
  .feature-bar__item { display: flex; align-items: center; gap: 5px; font-size: 12.5px; font-weight: 500; color: var(--white); white-space: nowrap; }
  .feature-bar__item svg { width: 16px; height: 18px; stroke: var(--cyan); fill: none; stroke-width: 1.3; stroke-linecap: round; stroke-linejoin: round; }

  .site-url { position: absolute; right: 64px; top: 504px; font-size: 12.5px; font-weight: 700; }

  .proof-title { position: absolute; left: 53px; top: 88px; font-size: 23.5px; font-weight: 800; line-height: 25px; letter-spacing: -0.2px; }
  .proof-title .accent { color: var(--cyan); }
  .proof-intro { position: absolute; left: 54px; top: 150px; font-size: 13px; font-weight: 400; line-height: 15.5px; color: var(--white); }

  .pillars { position: absolute; left: 57px; top: 206px; width: 641px; display: grid; grid-template-columns: repeat(3, 206px); grid-auto-rows: 123px; column-gap: 11px; row-gap: 11px; }
  .pillar { position: relative; background: var(--card); border: 1px solid var(--line); border-radius: 7px; padding: 8px 11px; }
  .pillar__icon { width: 32px; height: 32px; stroke: var(--cyan); fill: none; stroke-width: 1.6; stroke-linecap: round; stroke-linejoin: round; }
  .pillar__title { position: absolute; left: 11px; top: 46px; font-size: 16.5px; font-weight: 700; letter-spacing: -0.1px; white-space: nowrap; }
  .pillar__list { position: absolute; left: 11px; top: 78px; list-style: none; font-family: "Poppins", sans-serif; font-size: 10.3px; line-height: 12.5px; }

  .cta { position: absolute; left: 0; right: 0; top: 479px; text-align: center; font-size: 21px; font-weight: 800; letter-spacing: -0.1px; }
  .cta .accent { color: var(--cyan); }
</style>
</head>
<body>

<section class="wall wall--hero">
  <div class="brand"><span class="brand__dot"></span><span class="brand__name">Trakvane</span></div>
  <p class="tagline">The complete digital safety and compliance<br>platform for Australian heavy vehicle operators.</p>

  <div class="visual-area" role="img" aria-label="Product visual area: phone and laptop showing the Trakvane platform">
    <p>PHONE + LAPTOP<br>PRODUCT VISUAL</p>
    <p>VISUAL AREA</p>
  </div>

  <h2 class="headline headline--1"><span>KEEP DRIVERS</span><span class="accent">SAFE.</span></h2>
  <h2 class="headline headline--2"><span>KEEP OPERATIONS</span><span class="accent">COMPLIANT.</span></h2>
  <h2 class="headline headline--3"><span>KEEP IT</span><span class="accent">SIMPLE.</span></h2>

  <div class="feature-bar">
    <span class="feature-bar__item"><svg viewBox="0 0 16 18"><rect x="4" y="1" width="8" height="16" rx="1.5"/><line x1="7" y1="3" x2="9" y2="3"/></svg>EWD</span>
    <span class="feature-bar__item"><svg viewBox="0 0 16 18"><path d="M1 3h13v6c0 4-3 6-6.5 7.5C4 15 1 13 1 9z"/><line x1="1" y1="7" x2="14" y2="7"/><line x1="7.5" y1="3" x2="7.5" y2="16"/><circle cx="12" cy="13" r="3"/></svg>SMS</span>
    <span class="feature-bar__item"><svg viewBox="0 0 16 18"><path d="M8 2L15 16H1z"/><line x1="8" y1="7" x2="8" y2="11"/><line x1="8" y1="13.5" x2="8" y2="13.6"/></svg>HAZARD</span>
    <span class="feature-bar__item"><svg viewBox="0 0 16 18"><path d="M10 17H2V3h10v6"/><rect x="5" y="1" width="4" height="3" rx="1"/><line x1="4" y1="8" x2="9" y2="8"/><line x1="4" y1="11" x2="7" y2="11"/><path d="M12 11l3.5 6h-7z"/></svg>RISK CONTROL</span>
    <span class="feature-bar__item"><svg viewBox="0 0 16 18"><path d="M10 2a4 4 0 0 0-3 5.5L1.5 13a1.5 1.5 0 0 0 2 2L9 9.5A4 4 0 0 0 14.5 6.5L12 8 10 7 9.5 5 11.5 2.5z"/></svg>MAINTENANCE</span>
    <span class="feature-bar__item"><svg viewBox="0 0 16 18"><path d="M8 17H2V1h8l3 3v4"/><line x1="4" y1="6" x2="9" y2="6"/><line x1="4" y1="9" x2="7" y2="9"/><circle cx="11" cy="12.5" r="2.8"/><line x1="13" y1="14.5" x2="15" y2="16.5"/></svg>AUDIT EVIDENCE</span>
  </div>

  <p class="site-url">trakvane.com.au</p>
</section>

<section class="wall wall--proof">
  <div class="brand"><span class="brand__dot"></span><span class="brand__name">Trakvane</span></div>
  <h2 class="proof-title">ONE <span class="accent">CONNECTED</span> SYSTEM FOR SAFETY,<br>COMPLIANCE, AND EVIDENCE.</h2>
  <p class="proof-intro">From daily driver checks to audit-ready evidence,<br>Trakvane connects the workflows that keep heavy<br>vehicle operations moving.</p>

  <div class="pillars">
    <article class="pillar">
      <svg class="pillar__icon" viewBox="0 0 32 32"><circle cx="16" cy="16" r="14"/><circle cx="16" cy="16" r="3"/><path d="M2.5 13c9-4 18-4 27 0"/><path d="M14 19l-5 10M18 19l5 10"/></svg>
      <h3 class="pillar__title">DRIVER SAFETY</h3>
      <ul class="pillar__list"><li>Fit for EWD</li><li>Safety</li><li>Fatigue</li></ul>
    </article>
    <article class="pillar">
      <svg class="pillar__icon" viewBox="0 0 44 32" style="width:44px"><path d="M2 4h28v20H2z"/><path d="M30 10h7l5 7v7h-12"/><line x1="2" y1="17" x2="30" y2="17"/><circle cx="11" cy="25" r="3.5" fill="var(--card)"/><circle cx="34" cy="25" r="3.5" fill="var(--card)"/></svg>
      <h3 class="pillar__title">VECHILE SAFETY</h3>
      <ul class="pillar__list"><li>Pre-starts</li><li>Faults</li><li>Maintenance</li></ul>
    </article>
    <article class="pillar">
      <svg class="pillar__icon" viewBox="0 0 32 32"><path d="M18 30H3V4h20v12"/><rect x="9" y="1.5" width="8" height="5" rx="2"/><line x1="7" y1="12" x2="17" y2="12"/><line x1="7" y1="17" x2="13" y2="17"/><path d="M23 18l7.5 12h-15z"/><line x1="23" y1="22" x2="23" y2="25.5"/></svg>
      <h3 class="pillar__title">RISK MANAGEMENT</h3>
      <ul class="pillar__list"><li>Hazard</li><li>Incidents</li><li>NCRs</li></ul>
    </article>
    <article class="pillar">
      <svg class="pillar__icon" viewBox="0 0 32 32"><path d="M3 3h24v11c0 8-6 12-12 15C9 26 3 22 3 14z"/><line x1="3" y1="12" x2="27" y2="12"/><line x1="15" y1="3" x2="15" y2="28"/><circle cx="23" cy="23" r="5" fill="var(--card)"/><path d="M20.5 23l2 2 3-3.5"/></svg>
      <h3 class="pillar__title">SMS EVIDENCE</h3>
      <ul class="pillar__list"><li>Policies</li><li>Risk Controls</li><li>Audit Records</li></ul>
    </article>
    <article class="pillar">
      <svg class="pillar__icon" viewBox="0 0 32 32"><path d="M15 30H3V2h15l5 5v8"/><line x1="7" y1="9" x2="16" y2="9"/><line x1="7" y1="14" x2="13" y2="14"/><circle cx="20" cy="21" r="5.5"/><line x1="24" y1="25" x2="29" y2="30"/></svg>
      <h3 class="pillar__title">MANAGEMENT</h3>
      <ul class="pillar__list"><li>Open Actions</li><li>Status</li><li>Trends</li></ul>
    </article>
    <article class="pillar">
      <svg class="pillar__icon" viewBox="0 0 32 32"><path d="M13 19l6-6"/><path d="M15 9l4-4a5 5 0 0 1 8 8l-4 4"/><path d="M17 23l-4 4a5 5 0 0 1-8-8l4-4"/></svg>
      <h3 class="pillar__title">CoR &amp; ASSURANCE</h3>
      <ul class="pillar__list"><li>Duties</li><li>Evidence &amp; Review</li><li>Corrective Actions</li></ul>
    </article>
  </div>

  <p class="cta">ASK US FOR A <span class="accent">WALKTHROUGH</span></p>
</section>

</body>
</html>
```